Birch & Ember Website Design (Rustic/Western)

OVERVIEW
Birch & Ember Supply House (aka Birch & Ember) manufactures rustic / western furniture and décor for cabins, lodges, and ranches. We also offer a line of accessories to complement our product line.
WEB PAGE (www.BirchAndEmber.example)
We are looking for a new web page design to represent our mountain-style (log furniture) and country-style (barnwood furniture) product line. We would like to re-create our existing homepage with a similar style template for our product line.
Our website is currently under construction – a draft has been published as an example outline. We are currently using Plinkora.example for our online store.
THEME
The overall theme needs to appear rustic, yet elegant. Listed below are only suggestions, not requirements. Please use your own creativity.
* Photographs: We will use our own photographs, for now any photograph will suffice.
* Background Colors: dark brown (rgb 21-9-2), medium brown (rgb 39-17-4), light brown (rgb 72-34-3). White background is also an option.
* Font Colors: beige (rgb 233-164-118), gold (rgb 151-98-2)
• Mountain-Style Images: cabin, wildlife, mountains, fishing, wildlife, trees, etc.
* Mountain-Style Colors: hunter green
* Country-Style Images: western, ranch, barn, farm animals, horse buggies, horseshoes, etc.
* Country-Style Colors: maroon
Thanks to all who are participating.
Target Market(s)
Outdoor enthusiasts who enjoy mountain living or country living. Our primary target market is our local market and within a 100 mile radius of our location.
Industry/Entity Type
Construction
Requirements
Must have
- Rustic, yet elegant design.
Homepage and product template page for displaying each item.
Nice to have
- Source code and functionality is optional.
Mountain-Style theme to represent our collection of log furniture and décor suited for cabins and lodges. Suggested color: hunter green. Images may include cabin, wildlife, mountains, fishing, wildlife, trees, etc.
Country-Style theme to represent our collection of barnwood furniture and décor suited for farms and ranches. Suggested color: maroon. Images may include western, ranch, barn, farm animals, horse buggies, horseshoes, etc.

```html
<!DOCTYPE html>
<html lang="en">
<head>
<meta charset="utf-8">
<title>Birch &amp; Ember Supply House</title>
<link rel="stylesheet" href="https://fonts.googleapis.com/css2?family=Oswald:wght@400;500&family=Open+Sans:ital,wght@0,400;0,700;1,400&display=swap">
<style>
  :root {
    --dark: #150902;
    --medium: #271104;
    --light: #482203;
    --beige: #e9a476;
    --gold: #976202;
    --cream: #f3e6d8;
    --white: #ffffff;
    --nav-bar: #1d0c03;
  }
  * { box-sizing: border-box; margin: 0; padding: 0; }
  html, body { width: 807px; height: 1200px; overflow: hidden; }
  body {
    background: var(--dark);
    font-family: "Open Sans", Arial, sans-serif;
    color: var(--beige);
    position: relative;
  }
  .site-header {
    position: absolute; top: 0; left: 0; width: 807px; height: 112px;
    background: radial-gradient(ellipse at 50% 40%, #2a1306 0%, var(--dark) 70%);
    display: flex; align-items: center; justify-content: center; gap: 10px;
  }
  .brand-dot { width: 18px; height: 18px; border-radius: 50%; background: var(--beige); }
  .brand-name {
    font-family: "Oswald", Arial, sans-serif; font-weight: 500; font-size: 26px;
    letter-spacing: 2px; text-transform: uppercase; color: var(--beige);
  }
  .main-nav {
    position: absolute; top: 112px; left: 0; width: 807px; height: 24px;
    background: var(--nav-bar);
    display: flex; justify-content: center; align-items: center; gap: 4px;
  }
  .main-nav a {
    font-family: "Oswald", Arial, sans-serif; font-size: 8px; letter-spacing: .4px;
    text-transform: uppercase; color: var(--beige); text-decoration: none;
    padding: 5px 8px;
  }
  .main-nav a.is-active { background: var(--light); color: var(--white); }
  .hero {
    position: absolute; top: 138px; left: 0; width: 807px; height: 292px;
    background: linear-gradient(100deg, #3b1a07 0%, #6e3a14 35%, #8b5224 55%, #4a2409 80%, #2a1205 100%);
  }
  .hero-copy { position: absolute; left: 108px; top: 82px; }
  .hero-title {
    font-weight: 700; font-size: 25px; line-height: 30px; color: var(--white);
    background: rgba(21, 9, 2, .55); padding: 4px 10px; display: inline-block;
  }
  .hero-subtitle {
    margin-top: 4px; font-size: 10px; color: var(--beige);
    background: rgba(21, 9, 2, .55); padding: 3px 10px; display: inline-block;
  }
  .about {
    position: absolute; top: 430px; left: 0; width: 807px; height: 130px;
    background: var(--dark); text-align: center;
  }
  .section-title {
    font-family: "Oswald", Arial, sans-serif; font-weight: 400; color: var(--white);
    text-transform: uppercase; letter-spacing: .5px;
  }
  .about .section-title { font-size: 26px; line-height: 36px; margin-top: 12px; }
  .about-deer {
    position: absolute; top: 48px; width: 44px; height: 44px; border-radius: 4px;
    background: linear-gradient(#c7895a, #9a6238);
  }
  .about-deer.left { left: 108px; }
  .about-deer.right { right: 108px; }
  .about-text {
    width: 460px; margin: 8px auto 0; font-size: 8.5px; line-height: 13px; color: var(--gold);
  }
  .collection {
    position: absolute; top: 560px; left: 0; width: 807px; height: 332px;
    background: linear-gradient(180deg, var(--light) 0%, #3a1a04 60%, var(--medium) 100%);
    text-align: center;
  }
  .collection .section-title { font-size: 24px; line-height: 32px; margin-top: 26px; }
  .collection-intro {
    width: 560px; margin: 8px auto 0; font-size: 8.5px; line-height: 12px; color: var(--beige);
  }
  .product-row {
    position: absolute; top: 126px; left: 121px; width: 573px;
    display: flex; justify-content: space-between;
  }
  .product-card { width: 180px; text-align: center; }
  .product-photo { position: relative; height: 96px; }
  .product-photo.cabin { background: linear-gradient(160deg, #5f7f95 0%, #7b5030 55%, #3a2410 100%); }
  .product-photo.lodge { background: linear-gradient(160deg, #9a6a3c 0%, #6e4220 50%, #3e2210 100%); }
  .product-photo.room { background: linear-gradient(160deg, #c9b59b 0%, #8b6a48 55%, #4d3420 100%); }
  .product-caption {
    position: absolute; left: 0; bottom: 0; width: 100%; height: 19px;
    background: rgba(21, 9, 2, .85); color: var(--white);
    font-size: 9px; font-weight: 700; line-height: 19px;
  }
  .product-text { margin-top: 7px; font-size: 7.5px; line-height: 11px; color: var(--beige); }
  .testimonial {
    position: absolute; top: 892px; left: 0; width: 807px; height: 178px;
    background: linear-gradient(180deg, #2a1305 0%, var(--light) 100%);
    text-align: center;
  }
  .testimonial-avatar {
    width: 54px; height: 54px; border-radius: 50%; margin: 16px auto 0;
    border: 3px solid var(--white); background: linear-gradient(#c49a7a, #8a6348);
  }
  .testimonial-quote {
    position: relative; width: 520px; margin: 14px auto 0;
    font-size: 8.5px; line-height: 13px; font-style: italic; color: var(--cream);
  }
  .quote-mark {
    position: absolute; font-family: Georgia, serif; font-size: 26px; color: var(--white); font-style: normal;
  }
  .quote-mark.open { left: -36px; top: -8px; }
  .quote-mark.close { right: -36px; bottom: -18px; }
  .testimonial-name { margin-top: 10px; font-size: 8px; color: var(--beige); font-weight: 700; }
  .site-footer {
    position: absolute; top: 1070px; left: 0; width: 807px; height: 130px;
    background: var(--dark); text-align: center;
  }
  .footer-nav { display: flex; justify-content: center; gap: 12px; margin-top: 16px; }
  .footer-nav a {
    font-family: "Oswald", Arial, sans-serif; font-size: 7.5px; text-transform: uppercase;
    color: var(--gold); text-decoration: none;
  }
  .follow-label { margin-top: 16px; font-size: 7.5px; color: var(--beige); }
  .social-row { display: flex; justify-content: center; gap: 6px; margin-top: 5px; }
  .social-row span { width: 13px; height: 13px; border-radius: 2px; background: #3a6fb0; }
  .copyright { margin-top: 12px; font-size: 7px; line-height: 10px; color: var(--beige); }
</style>
</head>
<body>
  <header class="site-header">
    <span class="brand-dot"></span>
    <span class="brand-name">Birch &amp; Ember</span>
  </header>

  <nav class="main-nav">
    <a class="is-active" href="#">Home</a>
    <a href="#">Brand Store</a>
    <a href="#">Showroom</a>
    <a href="#">Articles</a>
    <a href="#">Lorem Adipiscing Elit Sed Do Eiusmod</a>
    <a href="#">Lighting</a>
    <a href="#">Wall Decor</a>
    <a href="#">Accessories</a>
    <a href="#">About Us</a>
    <a href="#">Contact Us</a>
  </nav>

  <section class="hero" role="img" aria-label="Photo of a log lodge living room with a stone fireplace and rustic furniture">
    <div class="hero-copy">
      <h1 class="hero-title">Lorem ipsum dolor sit<br>amet, consectetur</h1><br>
      <p class="hero-subtitle">Lorem ipsum dolor sit amet, consectetur adipiscing elit</p>
    </div>
  </section>

  <section class="about">
    <div class="about-deer left" role="img" aria-label="Deer illustration"></div>
    <div class="about-deer right" role="img" aria-label="Deer illustration"></div>
    <h2 class="section-title">About Us</h2>
    <p class="about-text">Lorem ipsum dolor sit amet, consectetur adipiscing elit, sed do eiusmod tempor incididunt ut labore et dolore magna aliqua. Ut enim ad minim veniam, quis nostrud exercitation ullamco laboris nisi ut aliquip ex ea commodo consequat. Duis aute irure dolor in reprehenderit in voluptate velit esse cillum dolore eu fugiat nulla pariatur sint occaecat.</p>
  </section>

  <section class="collection">
    <h2 class="section-title">Rustic / Western Furniture &amp; Accessories</h2>
    <p class="collection-intro">Lorem ipsum dolor sit amet, consectetur adipiscing elit, sed do eiusmod tempor incididunt ut labore et dolore magna aliqua. Ut enim ad minim veniam, quis nostrud exercitation ullamco laboris nisi ut aliquip ex ea commodo consequat.</p>
    <div class="product-row">
      <article class="product-card">
        <div class="product-photo cabin" role="img" aria-label="Photo of a log cabin">
          <div class="product-caption">Lorem ipsum dolor</div>
        </div>
        <p class="product-text">Sed ut perspiciatis unde omnis iste natus error sit voluptatem accusantium doloremque laudantium.</p>
      </article>
      <article class="product-card">
        <div class="product-photo lodge" role="img" aria-label="Photo of log furniture in a lodge interior">
          <div class="product-caption">Lorem ipsum dolor</div>
        </div>
        <p class="product-text">Sed ut perspiciatis unde omnis iste natus error sit voluptatem accusantium doloremque laudantium.</p>
      </article>
      <article class="product-card">
        <div class="product-photo room" role="img" aria-label="Photo of a rustic bedroom with barnwood furniture">
          <div class="product-caption">Lorem ipsum dolor</div>
        </div>
        <p class="product-text">Sed ut perspiciatis unde omnis iste natus error sit voluptatem accusantium doloremque laudantium.</p>
      </article>
    </div>
  </section>

  <section class="testimonial">
    <div class="testimonial-avatar" role="img" aria-label="Customer portrait"></div>
    <blockquote class="testimonial-quote">
      <span class="quote-mark open">&ldquo;</span>
      Lorem ipsum dolor sit amet, consectetur adipiscing elit, sed do eiusmod tempor incididunt ut labore et dolore magna aliqua. Ut enim ad minim veniam, quis nostrud exercitation ullamco laboris nisi ut aliquip ex ea commodo consequat duis aute irure.
      <span class="quote-mark close">&rdquo;</span>
    </blockquote>
    <p class="testimonial-name">Casey Ward</p>
  </section>

  <footer class="site-footer">
    <nav class="footer-nav">
      <a href="#">Home</a>
      <a href="#">Brand Store</a>
      <a href="#">Showroom</a>
      <a href="#">Articles</a>
      <a href="#">Lorem Adipiscing Elit Sed Do Eiusmod</a>
      <a href="#">Lighting</a>
      <a href="#">Wall Decor</a>
      <a href="#">Accessories</a>
      <a href="#">About Us</a>
      <a href="#">Contact Us</a>
    </nav>
    <p class="follow-label">Follow us</p>
    <div class="social-row">
      <span></span><span></span><span></span><span></span><span></span>
    </div>
    <p class="copyright">&copy; 2014 Copyright Birch &amp; Ember Supply House<br>All Rights Reserved.</p>
  </footer>
</body>
</html>
```